Pictures required on web page

I would like change three existing pictures on my new website.

The site can be found here:
http://mossbottleroom.kestrelweb.com.au/

The three pictures to be changed are on the home page:
Purchase- Mixed Packs
Wine Club - Let Us Choose
Education- Wine Courses

I would like somthing stylish, classic and understated that fits in with the theme and feel of the site. I know stylish is a subjective thing. At the moment, the current picture makes the text difficult to read on a destop. Plus I don't think they are a perfect fit for our website anyway. I've attached a photo of our wine course room and also me in the store. Please, don't feel as though you have to use these pictures, but they're there if you want them. However I'm open to completely different photos/graphics to be used.

```html
<!DOCTYPE html>
<html lang="en">
<head>
<meta charset="utf-8">
<title>Vinecrest — Small winery specialist</title>
<link href="https://fonts.googleapis.com/css2?family=Roboto+Slab:wght@400;700&family=Roboto:wght@300;400;500&family=Arimo:wght@700&family=Tinos:wght@400;700&display=swap" rel="stylesheet">
<style>
  :root{
    --header-top:#2b3b5e;
    --header-bottom:#1e2a47;
    --menu-bar:#1a2133;
    --white:#ffffff;
    --muted:#c9d0de;
    --search-bg:#3a4d74;
    --search-border:#7283a6;
    --divider:#45557a;
    --shipping:#b94d4b;
    --shipping-line:#d98885;
    --newsletter:#22315a;
    --newsletter-line:#5d6e98;
    --page:#ffffff;
  }
  *{box-sizing:border-box;margin:0;padding:0}
  html,body{width:1200px;height:600px;overflow:hidden;background:var(--page)}
  body{position:relative;font-family:"Roboto",sans-serif;color:var(--white)}

  .site-header{position:absolute;left:0;top:0;width:1200px;height:95px;
    background:linear-gradient(var(--header-top),var(--header-bottom))}
  .brand{position:absolute;left:60px;top:4px}
  .brand-name{font-family:"Roboto Slab",serif;font-weight:700;font-size:40px;line-height:44px;letter-spacing:.5px}
  .brand-tagline{font-family:"Roboto",sans-serif;font-weight:300;font-size:21px;line-height:22px;color:var(--muted)}

  .search{position:absolute;left:367px;top:17px;width:317px;height:36px;
    background:var(--search-bg);border:1px solid var(--search-border);border-radius:3px}
  .search-label{position:absolute;left:14px;top:8px;font-size:16px;color:#b4bfd6}
  .search svg{position:absolute;right:10px;top:5px}

  .utility-nav{position:absolute;left:717px;top:10px;display:flex;list-style:none}
  .utility-nav li{width:88px;height:46px;text-align:center;font-size:13px;color:var(--muted);
    border-left:1px solid var(--divider);padding-top:4px}
  .utility-nav li:first-child{border-left:none}
  .utility-nav svg{display:block;margin:0 auto 9px}

  .main-nav{position:absolute;left:0;top:95px;width:1200px;height:52px;background:var(--menu-bar)}
  .main-nav ul{position:absolute;left:61px;top:14px;display:flex;list-style:none}
  .main-nav li{font-size:19.5px;margin-right:31px;color:var(--white)}
  .cart{position:absolute;left:977px;top:13px;display:flex;align-items:center;font-size:14px;color:var(--muted)}
  .cart svg{margin-right:10px}

  .tile{position:absolute;overflow:hidden;text-align:center}
  .tile-photo{position:absolute;inset:0}
  .tile-kicker{position:absolute;left:0;right:0;font-family:"Tinos",serif;font-weight:400;font-size:17px;letter-spacing:.5px}
  .tile-title{position:absolute;left:0;right:0;font-family:"Arimo",sans-serif;font-weight:700;font-size:31.5px}

  .tile-courses{left:38px;top:163px;width:359px;height:241px}
  .tile-courses .tile-photo{background:radial-gradient(ellipse at 72% 70%,#6e1420 0%,#2a0608 35%,#050203 70%)}
  .tile-courses .tile-kicker{top:82px}
  .tile-courses .tile-title{top:100px}

  .tile-club{left:418px;top:163px;width:360px;height:416px}
  .tile-club .tile-photo{background:linear-gradient(180deg,#ece8e4 0%,#d9d2cc 25%,#6b1a1c 35%,#4a1113 55%,#1b1414 75%,#cbc6c2 100%)}
  .tile-club .tile-kicker{top:130px}
  .tile-club .tile-title{top:164px;font-size:31px}
  .read-more{position:absolute;left:121px;top:311px;width:116px;height:33px;border:2px solid var(--white);
    background:#111;font-family:"Tinos",serif;font-weight:700;font-size:17px;line-height:29px}

  .tile-packs{left:801px;top:163px;width:359px;height:241px}
  .tile-packs .tile-photo{background:linear-gradient(120deg,#1a0406 0%,#5e0c12 40%,#9a1a22 70%,#5a0a10 100%)}
  .tile-packs .tile-kicker{top:82px}
  .tile-packs .tile-title{top:100px;font-size:31px}

  .promo{position:absolute;text-align:center}
  .promo-frame{position:absolute;left:22px;top:22px;right:22px;bottom:22px;border:1px solid}
  .promo-title{position:absolute;left:0;right:0;font-size:21px;letter-spacing:2.5px;font-weight:400}
  .promo-note{position:absolute;left:0;right:0;font-size:15px;letter-spacing:2px;font-weight:300}

  .promo-shipping{left:38px;top:420px;width:359px;height:161px;background:var(--shipping)}
  .promo-shipping .promo-frame{border-color:var(--shipping-line)}
  .promo-shipping .promo-title{top:56px}
  .promo-shipping .promo-note{top:87px}

  .promo-newsletter{left:801px;top:417px;width:359px;height:162px;background:var(--newsletter)}
  .promo-newsletter .promo-frame{border-color:var(--newsletter-line)}
  .promo-newsletter .promo-title{top:57px}
  .promo-newsletter .promo-note{top:87px;font-size:15.5px;letter-spacing:2.2px}
</style>
</head>
<body>
<header class="site-header">
  <div class="brand">
    <div class="brand-name">Vinecrest</div>
    <div class="brand-tagline">Small winery specialist.</div>
  </div>
  <div class="search">
    <span class="search-label">Search the Cellars</span>
    <svg width="26" height="26" viewBox="0 0 26 26" aria-hidden="true">
      <circle cx="10" cy="10" r="7.5" fill="none" stroke="#e8ecf4" stroke-width="2"/>
      <line x1="15.5" y1="15.5" x2="23" y2="23" stroke="#e8ecf4" stroke-width="3" stroke-linecap="round"/>
    </svg>
  </div>
  <ul class="utility-nav">
    <li><svg width="18" height="16" viewBox="0 0 18 16"><path d="M9 1 1 8h2v7h4v-5h4v5h4V8h2z" fill="#c9d0de"/></svg>HOME</li>
    <li><svg width="22" height="16" viewBox="0 0 22 16"><circle cx="11" cy="4" r="3.5" fill="#c9d0de"/><circle cx="4" cy="6" r="2.5" fill="#c9d0de"/><circle cx="18" cy="6" r="2.5" fill="#c9d0de"/><path d="M5 16c0-5 3-7 6-7s6 2 6 7zM0 15c0-4 2-5 4-5s3 1 3 1l-2 4zM22 15c0-4-2-5-4-5s-3 1-3 1l2 4z" fill="#c9d0de"/></svg>ABOUT</li>
    <li><svg width="18" height="17" viewBox="0 0 18 17"><rect x="1.5" y="3" width="15" height="13" fill="none" stroke="#c9d0de" stroke-width="1.6"/><rect x="1.5" y="3" width="15" height="3.5" fill="#c9d0de"/><rect x="4.5" y="0" width="2" height="4" fill="#c9d0de"/><rect x="11.5" y="0" width="2" height="4" fill="#c9d0de"/></svg>EVENTS</li>
    <li><svg width="17" height="17" viewBox="0 0 17 17"><circle cx="8.5" cy="8.5" r="5.5" fill="none" stroke="#c9d0de" stroke-width="4" stroke-dasharray="2.2 2.1"/><circle cx="8.5" cy="8.5" r="4.5" fill="#c9d0de"/><circle cx="8.5" cy="8.5" r="2" fill="#26345a"/></svg>ACCOUNT</li>
    <li><svg width="16" height="16" viewBox="0 0 16 16"><path d="M3 1 6 4 4.5 6.5c1 2 3 4 5 5L12 10l3 3-2 2C7 15 1 9 1 3z" fill="#c9d0de"/></svg>CONTACT</li>
  </ul>
</header>

<nav class="main-nav">
  <ul>
    <li>Red Wine</li><li>White Wine</li><li>Sparkling</li><li>Rosé</li>
    <li>Old &amp; Rare</li><li>Stickies</li><li>Imported</li><li>Wine Club</li>
  </ul>
  <div class="cart">
    <svg width="26" height="22" viewBox="0 0 26 22"><path d="M0 1h5l3 12h14l3-9H7" fill="none" stroke="#fff" stroke-width="2.4"/><path d="M7 4h18l-3 9H9z" fill="#fff"/><circle cx="10" cy="19" r="2.2" fill="#fff"/><circle cx="20" cy="19" r="2.2" fill="#fff"/></svg>
    Shopping cart is empty
  </div>
</nav>

<section class="tile tile-courses">
  <div class="tile-photo" role="img" aria-label="Photograph of a wine bottle, a glass of red wine and a bunch of red grapes on a black background"></div>
  <div class="tile-kicker">EDUCATION</div>
  <div class="tile-title">WINE COURSES</div>
</section>

<section class="tile tile-club">
  <div class="tile-photo" role="img" aria-label="Photograph of a hand holding a glass of red wine against a pale background"></div>
  <div class="tile-kicker">WINE CLUB</div>
  <div class="tile-title">Let Us CHOOSE</div>
  <div class="read-more">READ MORE</div>
</section>

<section class="tile tile-packs">
  <div class="tile-photo" role="img" aria-label="Photograph of red wine being poured from a bottle into a glass on a deep red background"></div>
  <div class="tile-kicker">PURCHASE</div>
  <div class="tile-title">MIXED PACKS</div>
</section>

<aside class="promo promo-shipping">
  <div class="promo-frame"></div>
  <div class="promo-title">FREE SHIPPING</div>
  <div class="promo-note">on orders over $200</div>
</aside>

<aside class="promo promo-newsletter">
  <div class="promo-frame"></div>
  <div class="promo-title">NEWSLETTER</div>
  <div class="promo-note">join the newsletter for specials</div>
</aside>
</body>
</html>
```